Thornvale Secure Business Cards

Need high quality business card designed around my company logo. Ideally the cards need to be a glossy black as the logo goes well with a black background.

The company is a Locksmithing business.

Domestic clients are Residential Home Owners and Landlords. Commercial clients are local businesses, estate agents, landlords, solicitors

Services offered :
Emergency Lock Out
New Lock Fitting & Replacement
High Security Upgrades
UPVC lock repairs
Mobile Key Cutting
Free Security Reviews

Qualificatons & Certifications:
Accredited Fenwick & Marrow NVQ Level 3, TQBA
Fully Insured
PVR Checked

Contact & Business Details:

Business Name : Thornvale Secure
Name: Rob Kessington
Tel: 01632 960481 Office / 07700900417 Mobile
Email: contact@thornvalesecure-demo.com
Website: www.thornvalesecure-demo.com

(please note that the website is currently under development and not available to view)

Industry/Entity Type

Locksmith

Contact Information for Business Card

Name: Rob Kessington

Services:
Emergency Lock Out
High Security Upgrades
UPVC lock repairs
Mobile Key Cutting
Free Security Reviews

Requirements
Must have
• Ideally the cards should be a glossy black as the logo stands out better on a black background.

Logo on front and the word LOCKSMITH should be incorporated into the front design of the card.

Qualifications & Certifications on the back ideally along the top / bottom of the card or split (I.e along the top “ Accredited : Fenwick & Marrow Level 3 , TQBA”
and along the bottom , “Fully Insured & PVR Checked”

Services offered ideally listed on the back of the card, preferably split into two columns. If possible the logo could also be incorporated onto the back of the card between the two services columns (I.e the services listed either side of the logo)
Nice to have
• On the back of the card, have the logo in the middle with the services listed either side of the logo I.e 3 services on left of logo and three to the right.

```html
<!DOCTYPE html>
<html lang="en">
<head>
<meta charset="utf-8">
<title>Thornvale Secure – Business Cards</title>
<link href="https://fonts.googleapis.com/css2?family=Arimo:wght@400;500&family=Tinos:wght@700&display=swap" rel="stylesheet">
<style>
  :root {
    --backdrop: #2b2c2e;
    --card: #1b1c1e;
    --gold: #e2b339;
    --gold-deep: #b8861f;
    --emboss: #2c2d30;
    --emboss-edge: #35363a;
  }
  html, body {
    margin: 0;
    width: 1200px;
    height: 1107px;
    overflow: hidden;
    background: var(--backdrop);
  }
  .stage {
    position: relative;
    width: 1200px;
    height: 1107px;
  }
  .card {
    position: absolute;
    top: 218px;
    width: 420px;
    height: 670px;
    background: var(--card);
    border-radius: 26px;
    box-shadow: 0 18px 40px rgba(0,0,0,.55);
    color: var(--gold);
    text-align: center;
    box-sizing: border-box;
  }
  .card--front { left: 150px; }
  .card--back { left: 630px; }

  .serif { font-family: "Tinos", "Times New Roman", serif; font-weight: 700; }
  .sans { font-family: "Arimo", Arial, sans-serif; }

  .brand {
    display: flex;
    flex-direction: column;
    align-items: center;
    gap: 14px;
  }
  .brand__ring {
    border-radius: 50%;
    border: 4px solid currentColor;
    box-sizing: border-box;
  }
  .brand__name {
    font-family: "Tinos", "Times New Roman", serif;
    font-weight: 700;
    text-transform: uppercase;
    letter-spacing: 1px;
  }

  .card--front .brand { padding-top: 62px; }
  .card--front .brand__ring { width: 96px; height: 96px; }
  .card--front .brand__name { font-size: 26px; }

  .role {
    margin-top: 30px;
    font-size: 40px;
    letter-spacing: 2px;
  }
  .person {
    margin-top: 42px;
    font-size: 29px;
    letter-spacing: 1px;
  }
  .contact-rule {
    position: relative;
    margin: 18px 36px 0;
    height: 34px;
  }
  .contact-rule::before {
    content: "";
    position: absolute;
    left: 0; right: 0; top: 50%;
    height: 1.5px;
    background: var(--gold-deep);
  }
  .contact-icons {
    position: relative;
    display: inline-flex;
    gap: 6px;
    padding: 0 8px;
    background: var(--card);
  }
  .contact-icons svg { width: 32px; height: 32px; display: block; }
  .contact-list {
    margin: 14px 0 0;
    padding: 0;
    list-style: none;
    font-size: 19px;
    line-height: 25px;
  }
  .rule {
    margin: 20px 36px 0;
    height: 1.5px;
    background: var(--gold-deep);
  }
  .credentials {
    display: flex;
    justify-content: center;
    align-items: center;
    gap: 22px;
    margin-top: 34px;
  }
  .credential { background: var(--gold); opacity: .9; }
  .credential--square { width: 62px; height: 52px; border-radius: 6px; }
  .credential--wide { width: 84px; height: 42px; border-radius: 8px; }
  .credential--round { width: 62px; height: 62px; border-radius: 50%; }

  .card--back .brand { padding-top: 110px; color: var(--emboss); }
  .card--back .brand__ring {
    width: 170px; height: 170px;
    border-width: 5px;
    box-shadow: 0 0 0 1px var(--emboss-edge);
  }
  .card--back .brand__name { font-size: 34px; }
  .back-heading {
    margin-top: 64px;
    font-size: 24px;
    line-height: 28px;
    letter-spacing: 1px;
  }
  .services {
    margin: 6px 0 0;
    padding: 0;
    list-style: none;
    font-size: 21px;
    line-height: 27px;
  }
</style>
</head>
<body>
<main class="stage">

  <section class="card card--front" aria-label="Business card front">
    <div class="brand">
      <div class="brand__ring" aria-hidden="true"></div>
      <div class="brand__name">Thornvale Secure</div>
    </div>
    <div class="role serif">LOCKSMITH</div>
    <div class="person serif">ROB KESSINGTON</div>

    <div class="contact-rule">
      <div class="contact-icons" aria-hidden="true">
        <svg viewBox="0 0 32 32"><circle cx="16" cy="16" r="15" fill="var(--gold)"/><path d="M10 12c0-2 1-3 3-3l1 3-2 1c1 3 3 5 6 6l1-2 3 1c0 2-1 3-3 3-5 0-9-4-9-9z" fill="var(--card)"/></svg>
        <svg viewBox="0 0 32 32"><circle cx="16" cy="16" r="15" fill="var(--gold)"/><rect x="11.5" y="7.5" width="9" height="17" rx="1.5" fill="none" stroke="var(--card)" stroke-width="2"/><circle cx="16" cy="21.5" r="1" fill="var(--card)"/></svg>
        <svg viewBox="0 0 32 32"><circle cx="16" cy="16" r="15" fill="var(--gold)"/><rect x="8" y="10.5" width="16" height="11" fill="none" stroke="var(--card)" stroke-width="2"/><path d="M8 11l8 6 8-6" fill="none" stroke="var(--card)" stroke-width="2"/></svg>
        <svg viewBox="0 0 32 32"><circle cx="16" cy="16" r="15" fill="var(--gold)"/><g fill="none" stroke="var(--card)" stroke-width="1.8"><circle cx="16" cy="16" r="8"/><ellipse cx="16" cy="16" rx="3.5" ry="8"/><path d="M8 16h16"/></g></svg>
      </div>
    </div>

    <ul class="contact-list sans">
      <li>01632 960481</li>
      <li>07700900417</li>
      <li>contact@thornvalesecure-demo.com</li>
      <li>www.thornvalesecure-demo.com</li>
    </ul>
    <div class="rule"></div>

    <div class="credentials" aria-label="Accreditations">
      <div class="credential credential--square" role="img" aria-label="Fenwick &amp; Marrow accreditation"></div>
      <div class="credential credential--wide" role="img" aria-label="TQBA certification"></div>
      <div class="credential credential--round" role="img" aria-label="Fully insured seal"></div>
      <div class="credential credential--square" role="img" aria-label="PVR checked"></div>
    </div>
  </section>

  <section class="card card--back" aria-label="Business card back">
    <div class="brand">
      <div class="brand__ring" aria-hidden="true"></div>
      <div class="brand__name">Thornvale Secure</div>
    </div>
    <div class="back-heading serif">DOMESTIC &amp;<br>COMMERCIAL LOCKSMITHS</div>
    <ul class="services sans">
      <li>Emergency Lock Out</li>
      <li>New Lock Fitting &amp; Replacement</li>
      <li>High Security Upgrades</li>
      <li>UPVC lock repairs</li>
      <li>Mobile Key Cutting</li>
      <li>Free Security Reviews</li>
    </ul>
  </section>

</main>
</body>
</html>
```